Ferlande Glues

Website for funeral directors see the original website: http://pates-ferlande.be
Target Market(s)
B2C
Coding
Coded - Design and coding required
Number of Pages Required
5+ page
Font styles to use
Serif
Sans Serif
Script
Colors
9d9d9d
757575
e667a6
eea4c8
e34197
Requirements
Must have
- Keep the architecture of the current site.
Nice to have
- A page with a list of people who have died. See example: https://www.maisonbrevant.be

```html
<!DOCTYPE html>
<html lang="fr">
<head>
<meta charset="utf-8">
<title>Ferlande Funérailles – Derniers décès</title>
<link href="https://fonts.googleapis.com/css2?family=Poppins:ital,wght@0,300;0,400;0,500;1,400&family=Tinos&display=swap" rel="stylesheet">
<style>
:root{
  --pink:#e667a6;
  --pink-deep:#e34197;
  --pink-soft:#eea4c8;
  --grey:#757575;
  --grey-light:#9d9d9d;
  --ink:#111;
  --text:#555;
}
*{margin:0;padding:0;box-sizing:border-box}
html,body{width:861px;height:1200px;overflow:hidden;background:#fff;font-family:'Poppins',sans-serif;color:var(--ink)}
.page{position:relative;width:861px;height:1200px}
.header{height:72px;position:relative}
.brand{position:absolute;left:103px;top:22px;display:flex;align-items:center;gap:8px}
.brand-mark{width:22px;height:22px;border-radius:50%;background:var(--ink)}
.brand-name{font-size:17px;font-weight:500;color:var(--ink)}
.contact{position:absolute;right:103px;top:35px;display:flex;gap:16px;font-size:10px;font-weight:300}
.contact span{display:flex;align-items:center;gap:6px}
.nav{height:27px;background:var(--pink);display:flex;align-items:center;padding-left:110px;gap:0}
.nav a{color:#fff;text-decoration:none;font-size:9px;font-weight:300}
.nav a.current{font-weight:500;font-size:10px}
.quote{text-align:center;font-style:italic;font-size:16px;line-height:27px;margin-top:37px}
.section-title{text-align:center;margin-top:13px}
.section-title span{color:var(--pink);font-style:italic;font-size:15px;border-bottom:1px solid var(--pink);padding-bottom:1px}
.deaths{position:absolute;left:103px;top:272px;width:660px;display:grid;grid-template-columns:347px 313px;row-gap:27px}
.card{display:flex;height:136px}
.photo{width:136px;height:136px;flex:none}
.info{padding-left:23px;padding-top:11px}
.name{font-size:15px;font-weight:400;color:#333;letter-spacing:.2px}
.firm{font-size:10.5px;color:var(--text);margin-top:4px;font-weight:300}
.meta{font-size:10.5px;color:var(--text);margin-top:7px;line-height:15px;font-weight:300}
.btn{display:inline-block;margin-top:8px;border:1px solid var(--pink);font-family:'Tinos',serif;font-size:12px;color:#333;width:69px;height:28px;line-height:26px;text-align:center}
.load{position:absolute;left:393px;top:1103px;width:75px;height:28px;border:1px solid var(--pink);font-family:'Tinos',serif;font-size:12px;line-height:26px;text-align:center;color:#333}
.footer{position:absolute;left:0;bottom:0;width:861px;height:33px;background:var(--grey);color:#fff;font-size:9.5px;font-weight:300;text-align:center;line-height:33px}
</style>
</head>
<body>
<div class="page">
  <header class="header">
    <div class="brand"><div class="brand-mark"></div><div class="brand-name">Ferlande Funérailles</div></div>
    <div class="contact">
      <span><svg width="14" height="14" viewBox="0 0 24 24" fill="none" stroke="#111" stroke-width="1.5"><path d="M5 3h4l2 5-3 2a11 11 0 0 0 6 6l2-3 5 2v4a2 2 0 0 1-2 2A18 18 0 0 1 3 5a2 2 0 0 1 2-2z"/></svg>+32 (0) 61 / 48.17.30</span>
      <span><svg width="14" height="14" viewBox="0 0 24 24" fill="none" stroke="#111" stroke-width="1.5"><rect x="3" y="8" width="18" height="13"/><path d="M3 8l9 7 9-7M6 8V3h12v5"/></svg>contact@ferlande.be</span>
    </div>
  </header>
  <nav class="nav">
    <a href="#" style="margin-right:45px">Accueil</a>
    <a href="#" style="margin-right:47px">Notre Société</a>
    <a href="#" style="margin-right:47px">Que Faire En Cas De Décès?</a>
    <a href="#" style="margin-right:47px">Nos Services</a>
    <a href="#" style="margin-right:44px">Ils Nous Ont Quittés</a>
    <a href="#" class="current">Contact</a>
  </nav>
  <p class="quote">L’arbre doit la beauté de ses fruits à la force de son écorce<br>et à la sagesse de ses racines…</p>
  <h2 class="section-title"><span>DERNIERS DÉCÈS</span></h2>

  <section class="deaths">
    <div class="card"><div class="photo" role="img" aria-label="Portrait photo of the deceased" style="background:linear-gradient(#3d5a2c,#c9b7b3)"></div><div class="info"><div class="name">Marie DUVENT</div><div class="firm">Pompes Funèbres Vervalle</div><div class="meta">décédé le 06 juin 2019<br>domicilié à Haut-Sarville</div><a class="btn">Funerals</a></div></div>
    <div class="card"><div class="photo" role="img" aria-label="Portrait photo of the deceased" style="background:linear-gradient(#8a7a66,#2a2a2e)"></div><div class="info"><div class="name">Marie DUVENT</div><div class="firm">Pompes Funèbres Vervalle</div><div class="meta">décédé le 06 juin 2019<br>domicilié à Haut-Sarville</div><a class="btn">Funerals</a></div></div>
    <div class="card"><div class="photo" role="img" aria-label="Portrait photo of the deceased" style="background:linear-gradient(#f4f2ef,#a8a89a)"></div><div class="info"><div class="name">Marie DUVENT</div><div class="firm">Pompes Funèbres Vervalle</div><div class="meta">décédé le 06 juin 2019<br>domicilié à Haut-Sarville</div><a class="btn">Funerals</a></div></div>
    <div class="card"><div class="photo" role="img" aria-label="Portrait photo of the deceased" style="background:linear-gradient(#4e3b2a,#c9a23a)"></div><div class="info"><div class="name">Marie DUVENT</div><div class="firm">Pompes Funèbres Vervalle</div><div class="meta">décédé le 06 juin 2019<br>domicilié à Haut-Sarville</div><a class="btn">Funerals</a></div></div>
    <div class="card"><div class="photo" role="img" aria-label="Portrait photo of the deceased" style="background:linear-gradient(#f2f2f2,#2c3a6a)"></div><div class="info"><div class="name">Marie DUVENT</div><div class="firm">Pompes Funèbres Vervalle</div><div class="meta">décédé le 06 juin 2019<br>domicilié à Haut-Sarville</div><a class="btn">Funerals</a></div></div>
    <div class="card"><div class="photo" role="img" aria-label="Photo of the deceased on a motorcycle" style="background:linear-gradient(#4f7a3a,#9e1e24)"></div><div class="info"><div class="name">Marie DUVENT</div><div class="firm">Pompes Funèbres Vervalle</div><div class="meta">décédé le 06 juin 2019<br>domicilié à Haut-Sarville</div><a class="btn">Funerals</a></div></div>
    <div class="card"><div class="photo" role="img" aria-label="Black and white portrait photo of the deceased" style="background:linear-gradient(#3a3a3a,#d8d8d8)"></div><div class="info"><div class="name">Marie DUVENT</div><div class="firm">Pompes Funèbres Vervalle</div><div class="meta">décédé le 06 juin 2019<br>domicilié à Haut-Sarville</div><a class="btn">Funerals</a></div></div>
    <div class="card"><div class="photo" role="img" aria-label="Portrait photo of the deceased" style="background:linear-gradient(#8a8a86,#2e8aa8)"></div><div class="info"><div class="name">Marie DUVENT</div><div class="firm">Pompes Funèbres Vervalle</div><div class="meta">décédé le 06 juin 2019<br>domicilié à Haut-Sarville</div><a class="btn">Funerals</a></div></div>
    <div class="card"><div class="photo" role="img" aria-label="Portrait photo of the deceased" style="background:linear-gradient(#4a4a4a,#7fb8c4)"></div><div class="info"><div class="name">Marie DUVENT</div><div class="firm">Pompes Funèbres Vervalle</div><div class="meta">décédé le 06 juin 2019<br>domicilié à Haut-Sarville</div><a class="btn">Funerals</a></div></div>
    <div class="card"><div class="photo" role="img" aria-label="Black and white portrait photo of the deceased" style="background:linear-gradient(#9a9a9a,#3a4a7a)"></div><div class="info"><div class="name">Marie DUVENT</div><div class="firm">Pompes Funèbres Vervalle</div><div class="meta">décédé le 06 juin 2019<br>domicilié à Haut-Sarville</div><a class="btn">Funerals</a></div></div>
  </section>

  <a class="load">Load More</a>
  <footer class="footer">Copyright © 2019 Funeral Homes Ferlande Glues.</footer>
</div>
</body>
</html>
```